Accountant & CPA Website $100 bonus

We are designing a website for our client Tallow Ridge Accountants and CPAs. They are a new business and looking for a clean, modern website. The services they offer are siilar to: https://www.dvm-lqt.com/index.htm

We would like to see designs that use the black and the green mostly, with a hint of purple and grey. However, we do like to give our designers the freedom to be creative. If you see a different vison, feel free to express that.

Number of Pages Required

1 page

Font styles to use
Sans Serif

```html
<!DOCTYPE html>
<html lang="en">
<head>
<meta charset="utf-8">
<title>Tallow Ridge Accountants and CPAs</title>
<link href="https://fonts.googleapis.com/css2?family=Poppins:wght@400;500;600&family=Roboto+Condensed:wght@500;700&display=swap" rel="stylesheet">
<style>
:root{
  --green:#718c1f;
  --green-dark:#5f7718;
  --purple:#2b0f92;
  --ink:#111111;
  --grey:#555555;
  --paper:#f5f4f9;
  --sage:#eef0e4;
  --white:#ffffff;
}
*{margin:0;padding:0;box-sizing:border-box}
html,body{width:1200px;height:4090px;overflow:hidden}
body{position:relative;background:var(--paper);font-family:'Poppins',sans-serif;color:var(--ink)}
.abs{position:absolute}
.backdrop{position:absolute;left:0;top:0;width:1200px;height:4090px}
.btn{position:absolute;display:flex;align-items:center;justify-content:center;background:var(--green);color:var(--white);border-radius:30px;font-family:'Roboto Condensed',sans-serif;font-weight:700;font-size:15px;letter-spacing:.3px}

/* top bar */
.top-bar{left:0;top:0;width:1200px;height:34px;background:var(--purple)}
.badge-shape{left:60px;top:4px;width:68px;height:25px;border:2px solid var(--white);border-radius:3px}
.call-label{left:915px;top:10px;font-size:11px;color:var(--white)}
.call-icon{left:993px;top:4px;width:26px;height:26px;border-radius:50%;background:var(--green);display:flex;align-items:center;justify-content:center}
.call-number{left:1025px;top:3px;font-family:'Roboto Condensed',sans-serif;font-weight:500;font-size:22px;color:var(--green)}

/* header */
.brand{display:flex;align-items:center;gap:10px}
.brand-dot{width:16px;height:16px;border-radius:50%;background:var(--purple)}
.brand-name{font-family:'Roboto Condensed',sans-serif;font-weight:700;color:var(--green);letter-spacing:.5px}
.header-brand{left:60px;top:54px}
.header-brand .brand-name{font-size:34px}
.main-nav{left:406px;top:56px;display:flex;align-items:center;gap:26px;font-size:13px;color:var(--ink)}
.main-nav .home{background:var(--green);color:var(--white);border-radius:20px;padding:9px 21px}
.caret{display:inline-block;margin-left:6px;border-left:4px solid transparent;border-right:4px solid transparent;border-top:5px solid var(--ink);vertical-align:middle}

/* hero */
.hero-title{left:60px;top:250px;font-family:'Roboto Condensed',sans-serif;font-weight:700;font-size:54px;line-height:60px}
.hero-title .accent{color:var(--green)}
.hero-text{left:61px;top:381px;width:500px;font-size:15px;line-height:23px;color:#222}
.hero-btn{left:60px;top:444px;width:179px;height:44px}
.hero-photo{left:622px;top:170px;width:510px;height:435px;border-radius:90px 180px 90px 180px;background:linear-gradient(135deg,#6f7f8c,#c9ced3 45%,#e8e6e1 70%,#8e8a84)}
.deco-circle{border-radius:50%;background:var(--purple)}

/* welcome */
.welcome-eyebrow{left:637px;top:874px;font-size:14px;letter-spacing:1px}
.welcome-title{left:634px;top:898px;font-family:'Roboto Condensed',sans-serif;font-weight:700;font-size:42px;line-height:46px}
.welcome-title .accent{color:var(--green);font-size:37px}
.welcome-text{left:637px;top:1002px;width:460px;font-size:13px;line-height:22.6px;color:#333}
.welcome-btn{left:637px;top:1198px;width:127px;height:43px}
.cpa-circle{left:151px;top:775px;width:170px;height:170px;border-radius:50%;background:var(--purple);color:var(--white);display:flex;align-items:center;justify-content:center;font-family:'Roboto Condensed',sans-serif;font-weight:700;font-size:76px}

/* focus */
.focus-box{left:168px;top:1352px;width:864px;height:232px;border:2px solid var(--purple);border-radius:40px}
.focus-inner{left:182px;top:1364px;width:838px;height:208px;border-radius:34px;background:var(--white);box-shadow:0 6px 18px rgba(0,0,0,.06)}
.focus-title{left:182px;top:1398px;width:838px;text-align:center;font-family:'Roboto Condensed',sans-serif;font-weight:700;font-size:34px;line-height:41px}
.focus-btn{left:510px;top:1498px;width:180px;height:43px}

/* services */
.services-title{left:0;top:1752px;width:1200px;text-align:center;font-family:'Roboto Condensed',sans-serif;font-weight:700;font-size:42px;color:var(--white)}
.services-sub{left:0;top:1814px;width:1200px;text-align:center;font-size:15px;line-height:24px;color:var(--white)}
.service-card{width:528px;height:225px;background:var(--white);border-radius:6px}
.service-img{position:absolute;left:6px;top:6px;width:224px;height:213px;border-radius:4px 50% 50% 4px}
.service-body{position:absolute;left:256px;top:22px;width:250px}
.service-body h3{font-family:'Roboto Condensed',sans-serif;font-weight:700;font-size:21px;margin-bottom:12px;white-space:nowrap}
.service-body p{font-size:11.5px;line-height:21px;color:#777}
.learn{display:inline-block;margin-top:10px;font-family:'Roboto Condensed',sans-serif;font-size:15px;color:var(--green);text-decoration:underline}
.learn::after{content:"";display:inline-block;margin-left:6px;border-top:5px solid transparent;border-bottom:5px solid transparent;border-left:7px solid var(--green)}

/* features */
.feature{width:232px;height:238px;background:var(--white);border-radius:60px;text-align:center;padding-top:26px}
.feature svg{display:block;margin:0 auto 10px}
.feature h4{font-family:'Roboto Condensed',sans-serif;font-weight:700;font-size:18px;line-height:22px}
.feature p{margin-top:8px;font-size:12px;line-height:20px;color:#444}

/* consultation */
.consult-title{left:60px;top:2982px;font-family:'Roboto Condensed',sans-serif;font-weight:700;font-size:42px;line-height:46px}
.consult-title .accent{color:var(--green)}
.consult-text{left:64px;top:3087px;width:440px;font-size:13px;line-height:22px;color:#444}
.field{left:60px;width:509px;height:44px;background:var(--white);border-radius:4px;display:flex}
.field-icon{width:40px;background:var(--green);border-radius:4px 0 0 4px;display:flex;justify-content:center;padding-top:12px}
.field-label{padding:14px 0 0 18px;font-size:11px;color:#555}
.submit-btn{left:62px;top:3433px;width:98px;height:43px}
.consult-photo{left:659px;top:3028px;width:481px;height:412px;border-radius:0 60px 0 80px;background:linear-gradient(160deg,#d9dde0,#8a8f96 50%,#3d4a4a 80%,#c49a6c)}

/* footer */
.footer-brand{left:0;top:3712px;width:1200px;justify-content:center}
.footer-brand .brand-name{font-size:44px}
.footer-col{top:3816px;color:var(--white)}
.footer-col h5{font-family:'Roboto Condensed',sans-serif;font-weight:700;font-size:18px;margin-bottom:10px}
.footer-col li{list-style:none;font-size:12.5px;line-height:26px}
.contact-row{display:flex;gap:14px;margin-bottom:20px;font-size:12.5px;line-height:20px}
.contact-row .label{color:var(--green);font-size:14px}
.bottom-bar{left:0;top:4040px;width:1200px;height:50px;background:var(--green)}
.copyright{left:61px;top:4058px;font-size:12px;color:var(--white)}
.social{top:4048px;width:34px;height:34px;border:2px solid var(--white);border-radius:50%}
</style>
</head>
<body>

<svg class="backdrop" viewBox="0 0 1200 4090" aria-hidden="true">
  <defs>
    <linearGradient id="welcomeFade" gradientUnits="userSpaceOnUse" x1="0" y1="620" x2="0" y2="1290">
      <stop offset="0" stop-color="#718c1f"/>
      <stop offset=".35" stop-color="#a6b86a"/>
      <stop offset="1" stop-color="#eef0e4"/>
    </linearGradient>
    <linearGradient id="heroFade" x1="0" y1="0" x2="0" y2="1">
      <stop offset="0" stop-color="#f1f0f8"/>
      <stop offset="1" stop-color="#f7f6fa"/>
    </linearGradient>
  </defs>
  <rect x="0" y="34" width="1200" height="700" fill="url(#heroFade)"/>
  <path d="M0,745 C140,650 260,600 390,640 C520,680 560,780 760,748 C930,720 1020,860 1200,965 L1200,1720 L0,1720 Z" fill="url(#welcomeFade)"/>
  <path d="M0,1700 C200,1640 380,1745 600,1705 C800,1665 1000,1640 1200,1640 L1200,2440 C1000,2500 800,2420 520,2470 C300,2510 120,2500 0,2575 Z" fill="#718c1f"/>
  <path d="M0,3722 C200,3690 360,3745 600,3686 C760,3646 830,3542 1000,3540 C1100,3540 1160,3568 1200,3590 L1200,4040 L0,4040 Z" fill="#2b0f92"/>
</svg>

<!-- top bar -->
<div class="abs top-bar"></div>
<div class="abs badge-shape" aria-hidden="true"></div>
<div class="abs call-label">Call Us On :</div>
<div class="abs call-icon">
  <svg width="14" height="14" viewBox="0 0 24 24"><path d="M6.6 10.8a15 15 0 0 0 6.6 6.6l2.2-2.2a1 1 0 0 1 1-.25 11.4 11.4 0 0 0 3.6.6 1 1 0 0 1 1 1V20a1 1 0 0 1-1 1A17 17 0 0 1 3 4a1 1 0 0 1 1-1h3.5a1 1 0 0 1 1 1c0 1.25.2 2.45.6 3.6a1 1 0 0 1-.25 1z" fill="#fff"/></svg>
</div>
<div class="abs call-number">555 301 4826</div>

<!-- header -->
<div class="abs brand header-brand"><span class="brand-dot"></span><span class="brand-name">TALLOW RIDGE</span></div>
<nav class="abs main-nav">
  <span class="home">HOME</span>
  <span>TAX SEVICES<i class="caret"></i></span>
  <span>ACCOUNTING SERVICES<i class="caret"></i></span>
  <span>INDUSTRIES<i class="caret"></i></span>
  <span>ABOUT US<i class="caret"></i></span>
  <span>CONTACT</span>
</nav>

<!-- hero -->
<h1 class="abs hero-title"><span class="accent">Professional Accounting</span><br>And Tax Services</h1>
<p class="abs hero-text">Ledgerline is a leading company providing quality accounting &amp; tax services to businesses.</p>
<div class="btn hero-btn">FREE CONSULTATION</div>
<div class="abs deco-circle" style="left:987px;top:120px;width:60px;height:60px"></div>
<div class="abs" style="left:1100px;top:230px;width:40px;height:90px;border-radius:0 40px 40px 0;background:var(--purple)"></div>
<div class="abs" style="left:1100px;top:330px;width:40px;height:170px;background:var(--purple);border-radius:0 20px 20px 0"></div>
<div class="abs" style="left:987px;top:580px;width:60px;height:82px;border-radius:0 0 20px 20px;background:var(--purple)"></div>
<div class="abs deco-circle" style="left:810px;top:617px;width:62px;height:62px"></div>
<div class="abs hero-photo" role="img" aria-label="Photo of an accountant in a suit reviewing documents at a desk with a laptop"></div>

<!-- welcome -->
<svg class="abs" style="left:40px;top:840px" width="565" height="410" viewBox="0 0 565 410" role="img" aria-label="Photo of a hand with a pen over financial papers next to a calculator">
  <defs>
    <linearGradient id="calcTone" x1="0" y1="0" x2="1" y2="1">
      <stop offset="0" stop-color="#e4e8ee"/>
      <stop offset=".55" stop-color="#f7f8fa"/>
      <stop offset="1" stop-color="#9aa4b4"/>
    </linearGradient>
  </defs>
  <path d="M40,170 C90,110 170,120 250,90 C320,50 340,0 420,5 C510,10 560,90 560,180 C560,300 470,405 350,410 C240,412 150,380 80,320 C20,270 -5,220 40,170 Z" fill="url(#calcTone)"/>
</svg>
<div class="abs cpa-circle">CPA</div>
<div class="abs welcome-eyebrow">WELCOME TO</div>
<h2 class="abs welcome-title"><span class="accent">TALLOW RIDGE ACCOUNTANTS</span><br>AND CPAs</h2>
<p class="abs welcome-text">Lorem Ipsum has been the industry's standard dummy text ever since the 1500s, when an unknown printer took a galley of type and scrambled it to make a type specimen book. It has survived not only five centuries, but also the leap into electronic typesetting, remaining essentially unchanged. It was popularised in the 1960s with the release of Dryline sheets containing Lorem Ipsum passages, and more recently with desktop publishing software like Folio Layout including versions of Lorem Ipsum.</p>
<div class="btn welcome-btn">KNOW MORE</div>

<!-- focus -->
<div class="abs focus-box"></div>
<div class="abs focus-inner"></div>
<svg class="abs" style="left:536px;top:1318px" width="128" height="50" viewBox="0 0 128 50" aria-hidden="true">
  <rect x="0" y="0" width="128" height="50" fill="#f1f2ea"/>
  <line x1="0" x2="12" y1="34" y2="34" stroke="#2b0f92" stroke-width="2"/>
  <circle cx="12" cy="34" r="5" fill="#718c1f" stroke="#2b0f92" stroke-width="2"/>
  <line x1="116" x2="128" y1="34" y2="34" stroke="#2b0f92" stroke-width="2"/>
  <circle cx="116" cy="34" r="5" fill="#718c1f" stroke="#2b0f92" stroke-width="2"/>
  <circle cx="64" cy="30" r="14" fill="#2b0f92"/>
</svg>
<h2 class="abs focus-title">Focus on Running your Business and Leave the<br>Accounting to Us.</h2>
<div class="btn focus-btn">FREE CONSULTATION</div>

<!-- services -->
<h2 class="abs services-title">OUR SERVICES</h2>
<p class="abs services-sub">Ledgerline is a leading company providing quality<br>accounting &amp; tax services to businesses.</p>

<div class="abs service-card" style="left:60px;top:1912px">
  <div class="service-img" role="img" aria-label="Photo of a man working with a laptop and paperwork" style="background:linear-gradient(135deg,#3c4a5e,#cfd6dc 60%,#f1f1ee)"></div>
  <div class="service-body"><h3>TAX SERVICES</h3><p>Lorem Ipsum has been the industry's standard dummy text ever since the 1500s, when an unknown printer took a galley of type.</p><span class="learn">Learn More</span></div>
</div>
<div class="abs service-card" style="left:611px;top:1912px">
  <div class="service-img" role="img" aria-label="Photo of hands pointing at financial charts on a desk" style="background:linear-gradient(135deg,#c8ccd4,#f3f4f6 50%,#7fa3c8)"></div>
  <div class="service-body"><h3>ACCOUNTING SERVICES</h3><p>Lorem Ipsum has been the industry's standard dummy text ever since the 1500s, when an unknown printer took a galley of type.</p><span class="learn">Learn More</span></div>
</div>
<div class="abs service-card" style="left:60px;top:2160px">
  <div class="service-img" role="img" aria-label="Photo of a laptop with tax icons overlaid" style="background:linear-gradient(135deg,#e9e7e3,#a5a9ae 55%,#5a6068)"></div>
  <div class="service-body"><h3>INDUSTRIES</h3><p>Lorem Ipsum has been the industry's standard dummy text ever since the 1500s, when an unknown printer took a galley of type.</p><span class="learn">Learn More</span></div>
</div>
<div class="abs service-card" style="left:611px;top:2160px">
  <div class="service-img" role="img" aria-label="Photo of hands typing on a laptop keyboard" style="background:linear-gradient(135deg,#f2f4f7,#b9c6d6 55%,#7b8ea6)"></div>
  <div class="service-body"><h3>CLOUDLEDGER ACCOUNTING</h3><p>Lorem Ipsum has been the industry's standard dummy text ever since the 1500s, when an unknown printer took a galley of type.</p><span class="learn">Learn More</span></div>
</div>

<!-- features -->
<div class="abs feature" style="left:214px;top:2655px">
  <svg width="64" height="56" viewBox="0 0 64 56" aria-hidden="true"><path d="M32 4l16 6v12c0 11-7 18-16 22-9-4-16-11-16-22V10z" fill="#718c1f" stroke="#222" stroke-width="2"/><path d="M24 22l6 6 11-11" fill="none" stroke="#2b0f92" stroke-width="3"/><path d="M4 34l14-6 8 14-12 8z M60 34l-14-6-8 14 12 8z" fill="#718c1f" stroke="#222" stroke-width="2"/></svg>
  <h4>TRUSTED<br>ACCOUNTANTS</h4><p>Lorem ipsums simple text print type setting industry</p>
</div>
<div class="abs feature" style="left:484px;top:2655px">
  <svg width="64" height="56" viewBox="0 0 64 56" aria-hidden="true"><circle cx="36" cy="14" r="11" fill="#718c1f" stroke="#222" stroke-width="2"/><text x="36" y="19" text-anchor="middle" font-size="13" font-family="Poppins,sans-serif" fill="#2b0f92">$</text><path d="M4 36h8v16H4z" fill="#718c1f" stroke="#222" stroke-width="2"/><path d="M12 40c10-4 18-4 26 0h14c4 0 4 6 0 6H34M12 50c14 4 28 2 46-10" fill="none" stroke="#222" stroke-width="2"/></svg>
  <h4>REASONABLE<br>FEES</h4><p>Lorem ipsums simple text print type setting industry</p>
</div>
<div class="abs feature" style="left:754px;top:2655px">
  <svg width="64" height="56" viewBox="0 0 64 56" aria-hidden="true"><circle cx="26" cy="14" r="10" fill="none" stroke="#222" stroke-width="2"/><path d="M8 54c0-14 8-22 18-22s18 8 18 22z" fill="none" stroke="#222" stroke-width="2"/><circle cx="48" cy="36" r="10" fill="#718c1f" stroke="#222" stroke-width="2"/><text x="48" y="41" text-anchor="middle" font-size="12" font-family="Poppins,sans-serif" fill="#2b0f92">$</text></svg>
  <h4>FREE<br>CONSULTATION</h4><p>Lorem ipsums simple text print type setting industry</p>
</div>

<!-- consultation -->
<h2 class="abs consult-title"><span class="accent">GET A FREE</span><br>CONSULTATION TODAY!</h2>
<p class="abs consult-text">Fill out the contact form below and one of our experienced accountants will get in touch with you shortly.</p>

<div class="abs field" style="top:3153px"><span class="field-icon"><svg width="18" height="18" viewBox="0 0 24 24"><circle cx="12" cy="12" r="10" fill="none" stroke="#fff" stroke-width="2"/><circle cx="12" cy="10" r="3.5" fill="#fff"/><path d="M6 19c1.5-3 3.5-4 6-4s4.5 1 6 4" fill="#fff"/></svg></span><span class="field-label">Name *</span></div>
<div class="abs field" style="top:3209px"><span class="field-icon"><svg width="18" height="16" viewBox="0 0 24 18"><rect x="1" y="1" width="22" height="16" rx="2" fill="#fff"/><path d="M1 2l11 8 11-8" fill="none" stroke="#718c1f" stroke-width="2"/></svg></span><span class="field-label">Email *</span></div>
<div class="abs field" style="top:3264px"><span class="field-icon"><svg width="16" height="16" viewBox="0 0 24 24"><path d="M6.6 10.8a15 15 0 0 0 6.6 6.6l2.2-2.2a1 1 0 0 1 1-.25 11.4 11.4 0 0 0 3.6.6 1 1 0 0 1 1 1V20a1 1 0 0 1-1 1A17 17 0 0 1 3 4a1 1 0 0 1 1-1h3.5a1 1 0 0 1 1 1c0 1.25.2 2.45.6 3.6a1 1 0 0 1-.25 1z" fill="#fff"/></svg></span><span class="field-label">Phone *</span></div>
<div class="abs field" style="top:3322px;height:96px"><span class="field-icon"><svg width="20" height="18" viewBox="0 0 24 22"><path d="M12 2C6 2 2 5.5 2 10c0 2.4 1.2 4.5 3 6l-1 5 5-3c1 .3 2 .4 3 .4 6 0 10-3.6 10-8.4S18 2 12 2z" fill="#fff"/></svg></span><span class="field-label">Message*</span></div>
<div class="btn submit-btn">SUBMIT</div>
<div class="abs consult-photo" role="img" aria-label="Photo of a smiling accountant holding a tablet in an office"></div>

<!-- footer -->
<div class="abs brand footer-brand"><span class="brand-dot"></span><span class="brand-name">TALLOW RIDGE</span></div>

<div class="abs footer-col" style="left:61px">
  <h5>SERVICES</h5>
  <ul><li>Tax Services</li><li>Tax Planning</li><li>Tax Preparation</li><li>International Tax Services</li><li>IRS Tax Problem Resolution</li><li>Our Tax Services</li></ul>
</div>
<div class="abs footer-col" style="left:338px">
  <h5>ACCOUNTING</h5>
  <ul><li>Incorporation Services</li><li>Outsourced CFO Services</li><li>CloudLedger Accounting</li><li>Small Business Accounting</li><li>Our Accounting Services</li></ul>
</div>
<div class="abs footer-col" style="left:614px">
  <h5>INDUSTRIES</h5>
  <ul><li>Healthcare</li><li>Online Retail &amp; e-Commerce</li><li>Real Estate Accounting</li><li>Technology</li><li>Wholesale Manufacturing</li><li>Industries We Serve</li></ul>
</div>
<div class="abs footer-col" style="left:897px">
  <h5>CONTACT US</h5>
  <div class="contact-row">
    <svg width="20" height="26" viewBox="0 0 20 26" aria-hidden="true"><path d="M10 1a8 8 0 0 0-8 8c0 6 8 15 8 15s8-9 8-15a8 8 0 0 0-8-8z" fill="none" stroke="#718c1f" stroke-width="2"/><circle cx="10" cy="9" r="3" fill="#718c1f"/></svg>
    <div><div class="label">Address:</div>101 - lorem ipsum simple text print<br>type setting industry.</div>
  </div>
  <div class="contact-row" style="align-items:center">
    <svg width="20" height="20" viewBox="0 0 24 24" aria-hidden="true"><path d="M6.6 10.8a15 15 0 0 0 6.6 6.6l2.2-2.2a1 1 0 0 1 1-.25 11.4 11.4 0 0 0 3.6.6 1 1 0 0 1 1 1V20a1 1 0 0 1-1 1A17 17 0 0 1 3 4a1 1 0 0 1 1-1h3.5a1 1 0 0 1 1 1c0 1.25.2 2.45.6 3.6a1 1 0 0 1-.25 1z" fill="#718c1f"/></svg>
    <div style="font-size:15px">555 301 4826</div>
  </div>
</div>

<div class="abs bottom-bar"></div>
<div class="abs copyright">©TALLOW RIDGE ACCOUNTANTS AND CPAs - 2023 All rights reserved.</div>
<div class="abs social" style="left:1018px" aria-hidden="true"></div>
<div class="abs social" style="left:1061px" aria-hidden="true"></div>
<div class="abs social" style="left:1104px" aria-hidden="true"></div>

</body>
</html>
```